Icon Selection Project for Graphic Designer

We need a graphic designer to find a series of 6 icons to be used as website navigation/action bar for a website that are redesigning. I am putting details into the attached file.

Target Market(s)

People interested in reading daily inspirational quotes

Requirements
Must have
• White icons that are easy to understand

```html
<!DOCTYPE html>
<html lang="en">
<head>
<meta charset="utf-8">
<title>Brightline Sayings – Daily Quote</title>
<link rel="stylesheet" href="https://fonts.googleapis.com/css2?family=Roboto:wght@400;500;700&family=Kalam:wght@400&display=swap">
<style>
  :root {
    --ink: #ffffff;
    --accent: #f0a02a;
    --sky-top: #35323b;
    --sky-mid: #54495a;
    --sky-glow: #8c6b72;
    --ridge: #3b2f2b;
    --valley: #1f1917;
  }
  * { margin: 0; padding: 0; box-sizing: border-box; }
  html, body { width: 1200px; height: 477px; overflow: hidden; }
  body { font-family: "Roboto", Arial, sans-serif; color: var(--ink); }

  .hero { position: relative; width: 1200px; height: 477px; overflow: hidden; }
  .hero__backdrop {
    position: absolute; inset: 0;
    background: linear-gradient(180deg,
      var(--sky-top) 0%, var(--sky-mid) 38%, var(--sky-glow) 56%,
      var(--ridge) 72%, var(--valley) 100%);
  }

  .brand {
    position: absolute; left: 28px; top: 20px;
    display: flex; align-items: center; gap: 10px;
    font-size: 31px; font-weight: 400; letter-spacing: 0.3px;
  }
  .brand__dot { width: 10px; height: 10px; border-radius: 50%; background: var(--ink); }

  .action-bar {
    position: absolute; top: 40px; right: 78px;
    display: flex; list-style: none;
  }
  .action {
    width: 76px; display: flex; flex-direction: column; align-items: center;
  }
  .action svg { width: 48px; height: 48px; fill: none; stroke: var(--ink); stroke-width: 2.2; stroke-linecap: round; stroke-linejoin: round; }
  .action__label { font-family: "Kalam", "Comic Sans MS", cursive; font-size: 15px; margin-top: 6px; line-height: 1; }

  .saved-mark { position: absolute; left: 1062px; top: 126px; width: 44px; height: 44px; }
  .saved-mark path { fill: none; stroke: var(--accent); stroke-width: 2.4; stroke-linejoin: round; }

  .nav-prev { position: absolute; left: 14px; top: 232px; width: 16px; height: 28px; }
  .nav-prev path { fill: none; stroke: var(--ink); stroke-width: 2; }

  .quote { position: absolute; left: 0; right: 0; top: 212px; text-align: center; }
  .quote__text { font-size: 18.5px; font-weight: 400; text-shadow: 0 1px 3px rgba(0,0,0,.4); }
  .quote__author { margin-top: 20px; font-size: 15.5px; font-weight: 500; font-style: normal; display: block; }

  .topic { position: absolute; left: 0; right: 0; top: 419px; text-align: center; font-size: 18px; font-weight: 700; }
</style>
</head>
<body>
<main class="hero">
  <div class="hero__backdrop" role="img" aria-label="Photograph of a starry night sky over a dark mountain valley"></div>

  <header class="brand"><span>Brightline Sayings</span><span class="brand__dot"></span></header>

  <ul class="action-bar">
    <li class="action">
      <svg viewBox="0 0 48 48"><circle cx="10" cy="36" r="6"/><circle cx="38" cy="36" r="6"/><circle cx="30" cy="10" r="6"/><path d="M16 36h16M13 31l13-16M32 16l4 14"/></svg>
      <span class="action__label">Share</span>
    </li>
    <li class="action">
      <svg viewBox="0 0 48 48"><path d="M6 22c0-10 8-16 20-16s18 6 18 14-8 14-18 14c-4 0-7-1-9-2L6 42l5-11c-3-2-5-5-5-9z"/><path d="M22 17c-3 1-4 4-3 7M30 17c-3 1-4 4-3 7"/></svg>
      <span class="action__label">My Quotes</span>
    </li>
    <li class="action">
      <svg viewBox="0 0 48 48"><path d="M6 20v8h6l14 9V11L12 20z"/><path d="M9 28l3 9h4l-2-8M31 18c2 3 2 9 0 12M35 14c4 5 4 15 0 20M39 11c5 7 5 19 0 26"/></svg>
      <span class="action__label">Subscribe</span>
    </li>
    <li class="action">
      <svg viewBox="0 0 48 48"><rect x="10" y="4" width="28" height="40" rx="2"/><rect x="14" y="11" width="5" height="5"/><rect x="14" y="20" width="5" height="5"/><rect x="14" y="29" width="5" height="5"/><path d="M22 13h12M22 22h12M22 31h12M15 13l2 2 4-5"/></svg>
      <span class="action__label">Topics</span>
    </li>
    <li class="action">
      <svg viewBox="0 0 48 48"><path d="M6 24c0-9 8-13 18-13h12v-5l8 9-8 9v-5H24c-6 0-10 2-12 6"/><path d="M42 24c0 9-8 13-18 13H12v5l-8-9 8-9v5h12c6 0 10-2 12-6"/></svg>
      <span class="action__label">Radom</span>
    </li>
    <li class="action">
      <svg viewBox="0 0 48 48"><path d="M24 42C10 32 4 24 4 16c0-6 5-10 10-10 5 0 8 3 10 7 2-4 5-7 10-7s10 4 10 10c0 8-6 16-20 26z"/></svg>
      <span class="action__label">Favorite</span>
    </li>
  </ul>

  <svg class="saved-mark" viewBox="0 0 48 48" aria-label="Saved as favorite"><path d="M24 42C10 32 4 24 4 16c0-6 5-10 10-10 5 0 8 3 10 7 2-4 5-7 10-7s10 4 10 10c0 8-6 16-20 26z"/></svg>

  <svg class="nav-prev" viewBox="0 0 16 28" aria-label="Previous quote"><path d="M14 1L2 14l12 13"/></svg>

  <blockquote class="quote">
    <p class="quote__text">The soul exists independent of the body, and continues after the body dies, taking up a new spiritual body.</p>
    <cite class="quote__author">Brother Anselm Vire</cite>
  </blockquote>

  <p class="topic">Topic: Life Beyond Death</p>
</main>
</body>
</html>
```